Electrical panel service sticker w Bucket truck & Logo

We have a rather plain sticker we put on lighting panels to remind customers who to call for service. We want to redesign them with brushed aluminum background. We want a remake of the sticker with the outline of a bucket truck. You'll need to find or draw the outling of a bucket truck maybe with the boom up slightly as we will get these stickers die cut.

We want LOGO with Ph.# and Email.
Electrical * Lighting * Sign Service

Target Market(s)

Commercial property managers

Industry/Entity Type

Property Management

Requirements
Must have
• Bucket Truck Outline

```html
<!DOCTYPE html>
<html lang="en">
<head>
<meta charset="utf-8">
<title>Brightway Maintenance – Panel Service Sticker</title>
<link rel="stylesheet" href="https://fonts.googleapis.com/css2?family=Roboto+Condensed:wght@700;800&display=swap">
<style>
  :root {
    --ink: #111111;
    --alu-light: #f4f4f4;
    --alu-mid: #d9d9d9;
    --alu-dark: #bdbdbd;
    --streak: rgba(150,150,150,0.18);
    --truck-dark: #2a2a2a;
    --truck-light: #6a6a6a;
  }
  html, body {
    margin: 0;
    padding: 0;
    width: 1200px;
    height: 900px;
    overflow: hidden;
  }
  .sticker {
    position: relative;
    width: 1200px;
    height: 900px;
    overflow: hidden;
    font-family: "Roboto Condensed", "Arial Narrow", sans-serif;
    color: var(--ink);
    background:
      repeating-linear-gradient(180deg, transparent 0 3px, var(--streak) 3px 4px, transparent 4px 9px),
      radial-gradient(ellipse at 55% 50%, var(--alu-light) 0%, var(--alu-mid) 60%, var(--alu-dark) 100%);
  }
  .truck-illustration {
    position: absolute;
    left: 615px;
    top: 72px;
    width: 385px;
    height: 505px;
    background: linear-gradient(160deg, var(--truck-light), var(--truck-dark));
    border-radius: 6px;
  }
  .brand-name {
    position: absolute;
    right: 600px;
    top: 300px;
    margin: 0;
    text-align: right;
    font-weight: 800;
    text-transform: uppercase;
    line-height: 0.95;
    color: var(--ink);
  }
  .brand-name .line-main { display: block; font-size: 98px; letter-spacing: -1px; }
  .brand-name .line-sub { display: block; font-size: 54px; margin-top: 10px; }
  .contact {
    position: absolute;
    left: 0;
    top: 604px;
    width: 1196px;
    text-align: center;
    text-transform: uppercase;
    font-weight: 700;
  }
  .contact-phone {
    margin: 0;
    font-size: 124px;
    line-height: 1;
    letter-spacing: 1px;
  }
  .contact-email {
    margin: 10px 0 0;
    font-size: 44px;
    line-height: 1.1;
  }
  .service-list {
    margin: 10px 0 0;
    font-size: 44px;
    line-height: 1.1;
    word-spacing: 6px;
  }
</style>
</head>
<body>
  <main class="sticker">
    <div class="truck-illustration" role="img" aria-label="Outline illustration of a bucket truck with its boom raised"></div>

    <h1 class="brand-name">
      <span class="line-main">Brightway</span>
      <span class="line-sub">Maintenance</span>
    </h1>

    <section class="contact">
      <p class="contact-phone">888-555-0142</p>
      <p class="contact-email">service@brightwaylighting.com</p>
      <p class="service-list">Electrical • Lighting • Sign Service</p>
    </section>
  </main>
</body>
</html>
```